Performance Coaching business needs brochure design

I need a brochure designed that will be given to attendants at an IT / Accountancy conference.
Aim: The brochure is to encourage people to take up the offer that will be on there.
My business: Velmora Vitality Coaching. I coach people in corporate jobs how to improve performance through keeping fitn and healthy.
The brochure: I will post a list of notes (2 pages) I have and the winning designer is to use these notes to take out the most important points and create a powerful, enticing brochure that meets the following guidlines:
Why staff health is important to business? You will quote stats and reasons why it is important.
What staff want from their employer?
What I do?
Case study
Enticing Offer
The winning design will use powerful images, and will be light on words. The words used will answer the above points (these points dont't necessarily need to be on the brochure in the wording I have used here).
You can use my website www.velmoravitalitycoaching.example for ideas.
Updates
Apologies but I have been advised of a slight change. I now require A4 size design. It needs to go into a folder with a lot of other information. My new requirements are:
a) 2-3 pages max. either 1 front and back and an offer page, or 2 -3 single sided pages. whatever looks best
b) page or section 1 must be about why personal health/wellbeing is important to business. Include stats from my handouts as well as reasons why
c) section 2 is about what benefit health is to staff (eg....they get more from their company, they are better at their job, their performance is enhanced etc
d) page or section 3 must include about me (from my website www.velmoravitalitycoaching.example) and results from KWT
d) section 4 is the offer to KWT delegates.
FYI KWT (company holding the conference) website is www.kwt-onward.example use it for their logo if you need
This format has been confirmed and aplogies for the change
Target Market(s)
Accountancy firms.
Industry/Entity Type
Health
Requirements
Must have
- Can be either a fold up style brochure or a flyer with front & back. Must be easy to print as I will need to print it as soon as possible.
The images supplied are just a guide...use if you like
Nice to have
- I'd like to see a design the portrays success, change, health, simplicity, clarity.

```html
<!DOCTYPE html>
<html lang="en">
<head>
<meta charset="utf-8">
<title>Velmora Vitality Coaching – Brochure</title>
<link rel="stylesheet" href="https://fonts.googleapis.com/css2?family=Righteous&family=Open+Sans:wght@400;600;700&display=swap">
<style>
  :root {
    --bg: #e9e9ea;
    --ink: #111111;
    --paper: #ffffff;
    --orange: #f07a28;
    --orange-deep: #b9480e;
    --orange-soft: #f5b487;
    --green: #8fd14f;
    --green-deep: #3f741a;
    --green-soft: #bfe58f;
    --lavender: #a9b1e6;
    --lavender-deep: #34376e;
    --lavender-soft: #c9cff2;
    --photo-suit: #3a3030;
    --photo-group: #7b6a80;
  }
  * { box-sizing: border-box; margin: 0; padding: 0; }
  html, body { width: 1200px; height: 900px; overflow: hidden; }
  body {
    background: var(--bg);
    font-family: "Open Sans", Arial, sans-serif;
    position: relative;
  }
  .page {
    position: absolute;
    top: 185px;
    width: 375px;
    height: 530px;
    overflow: hidden;
    box-shadow: 0 4px 14px rgba(0,0,0,0.18);
  }
  .page--offer { left: 12px; background: var(--orange); }
  .page--health { left: 412px; background: var(--green); }
  .page--staff { left: 812px; background: var(--lavender); }
  .page > * { position: absolute; }

  .callout {
    background: var(--ink);
    color: var(--paper);
    border-radius: 8px;
    padding: 7px 10px;
    font-size: 10.5px;
    font-weight: 600;
    line-height: 1.3;
  }
  .callout__label { font-weight: 700; }
  .page--offer .callout__label { color: var(--orange); }
  .page--health .callout__label { color: var(--green); }

  .headline {
    font-family: "Righteous", "Arial Black", sans-serif;
    color: var(--ink);
    line-height: 1;
  }
  .headline--boxed span { background: var(--paper); padding: 0 4px; }
  .display {
    font-family: "Righteous", "Arial Black", sans-serif;
    line-height: 1;
    white-space: nowrap;
    -webkit-text-stroke: 2px var(--paper);
    paint-order: stroke fill;
  }
  .body-copy { font-size: 9px; line-height: 1.4; }

  /* Orange page */
  .page--offer .callout--testimonial { top: 18px; left: 90px; right: 18px; }
  .page--offer .headline--what { top: 80px; left: 18px; font-size: 38px; }
  .page--offer .display { top: 104px; left: 110px; font-size: 100px; color: var(--orange-soft); }
  .page--offer .body-copy { top: 214px; left: 18px; right: 18px; color: var(--orange-deep); }
  .page--offer .callout--visit { top: 290px; left: 18px; right: 18px; font-size: 8.5px; word-break: break-all; }
  .page--offer .headline--offer { top: 342px; left: 18px; font-size: 42px; }
  .offer-panel {
    top: 434px; left: 0; right: 0; bottom: 0;
    background: var(--paper);
    padding: 8px 18px;
    font-size: 8px; line-height: 1.35; color: #333;
  }

  /* Green page */
  .page--health .callout { top: 12px; left: 18px; width: 260px; }
  .page--health .headline--why { top: 86px; left: 18px; font-size: 34px; }
  .page--health .display { top: 118px; left: 18px; font-size: 86px; color: var(--green-soft); }
  .page--health .headline--business { top: 212px; left: 80px; font-size: 31px; }
  .page--health .body-copy { top: 286px; left: 18px; width: 220px; color: var(--green-deep); }
  .photo--advisor {
    top: 270px; left: 250px; width: 110px; height: 160px;
    border-radius: 50px 50px 6px 6px;
    background: linear-gradient(180deg, #b9d99a 0%, var(--photo-suit) 55%, #1e1a1a 100%);
  }
  .stats-card {
    top: 440px; left: 18px; width: 300px;
    background: var(--paper); border-radius: 12px;
    padding: 10px 14px;
  }
  .stats-card__title { font-size: 10px; font-weight: 700; color: var(--green-deep); line-height: 1.25; }
  .stats-card__list { list-style: none; font-size: 11px; color: var(--ink); margin-top: 4px; line-height: 1.4; }
  .stats-card__list b { font-weight: 700; }

  /* Lavender page */
  .page--staff .headline--what { top: 22px; left: 18px; font-size: 30px; }
  .page--staff .display { top: 10px; left: 130px; font-size: 86px; color: var(--lavender-soft); }
  .page--staff .headline--want { top: 100px; left: 18px; font-size: 30px; }
  .page--staff .headline--need { top: 132px; left: 18px; font-size: 74px; }
  .page--staff .callout { top: 130px; right: 0; width: 118px; border-radius: 8px 0 0 8px; font-size: 9.5px; }
  .page--staff .body-copy { top: 226px; left: 18px; width: 205px; color: var(--lavender-deep); }
  .brand {
    top: 238px; right: 14px; width: 128px;
    background: var(--paper); padding: 8px; text-align: left;
  }
  .brand__name { display: flex; align-items: center; gap: 6px; font-size: 11px; font-weight: 700; color: var(--ink); line-height: 1.15; }
  .brand__mark { width: 10px; height: 10px; background: var(--ink); flex: none; }
  .brand__url { font-size: 6.5px; color: var(--ink); margin-top: 4px; word-break: break-all; }
  .benefits-card {
    top: 366px; left: 18px; width: 180px;
    background: var(--paper); border-radius: 12px; padding: 10px 12px;
  }
  .benefits-card__title { font-size: 9.5px; font-weight: 700; color: var(--lavender); line-height: 1.25; }
  .benefits-card__list { list-style: none; font-size: 11px; color: var(--ink); line-height: 1.4; margin-top: 4px; }
  .photo--team {
    top: 340px; left: 210px; width: 150px; height: 190px;
    border-radius: 70px 70px 0 0;
    background: linear-gradient(180deg, #d3c1b3 0%, var(--photo-group) 55%, #4a3c55 100%);
  }
</style>
</head>
<body>

<section class="page page--offer">
  <p class="callout callout--testimonial"><span class="callout__label">Testimonials:</span> 65% of people in KWT are now doing more exercise than they were 12 months ago.</p>
  <h2 class="headline headline--boxed headline--what"><span>What I</span></h2>
  <p class="display">do?</p>
  <p class="body-copy">I provide your company with an opportunity to reduce the high cost of absenteeism and presenteeism. By doing this, you get to position your business so it attracts and retains the highest quality of staff, at the same time as increasing revenue. You become more, when your staff become more.</p>
  <p class="callout callout--visit"><span class="callout__label">Visit</span><br>http://www.velmoravitalitycoaching.example/presentation.html</p>
  <h2 class="headline headline--boxed headline--offer"><span>The</span><br>offer:</h2>
  <div class="offer-panel">To learn more about how I can help you stay ahead of the pack, I have put together an offer to KWT delegates. The first 15 companies to contact me, I will come to your business and assess its suitability to meet the current demands. For this to occur I will require some information, which will remain confidential of course. I will come to your office, run through things for you, so you can see where you are at now and where you want to get to. I will also outline how Velmora Vitality Coaching may be able to assist you.</div>
</section>

<section class="page page--health">
  <p class="callout"><span class="callout__label">Dana Whitlow:</span><br>“CEOs for decades have been repeating a false story by stating: The workers physical body is not business relevant”</p>
  <h2 class="headline headline--boxed headline--why"><span>Why is</span></h2>
  <p class="display">health</p>
  <h2 class="headline headline--business">important to<br>business?</h2>
  <p class="body-copy">Health is the missing cog. We have business coaching and more recently EQ (emotional) coaching. For staff to function at their optimum, they must be healthy and have reasonable energy. To think otherwise is false. Health coaching can provide the missing link to your staffs performance.</p>
  <div class="photo photo--advisor" role="img" aria-label="Photo of a smiling businesswoman in a dark suit holding a red folder"></div>
  <div class="stats-card">
    <p class="stats-card__title">Studies show successful corporate health problems can create:</p>
    <ul class="stats-card__list">
      <li>26.8% <b>reduction</b> in absenteeism</li>
      <li>$5.81 <b>savings</b> on every dollar invested</li>
    </ul>
  </div>
</section>

<section class="page page--staff">
  <h2 class="headline headline--what">What</h2>
  <p class="display">staff</p>
  <h2 class="headline headline--want">want and</h2>
  <h2 class="headline headline--need">need?</h2>
  <p class="callout"><span class="callout__label">The work force is:</span> looking elsewhere else when needs are not taken care of</p>
  <p class="body-copy">The line between home and work has become more blurred. As a result, the work environment needs to provide as much as possible to offset the melting line of work and home. Otherwise staff will go somewhere that does provide the right benefits. They need &amp; want to remain fit and healthy as staff don't want to be worked into the ground. You can give them the piece that is missing. Make their lives better not worse.</p>
  <div class="brand">
    <p class="brand__name"><span class="brand__mark"></span>Velmora Vitality Coaching</p>
    <p class="brand__url">www.velmoravitalitycoaching.example</p>
  </div>
  <div class="benefits-card">
    <p class="benefits-card__title">If your staff are fit healthy you can expect:</p>
    <ul class="benefits-card__list">
      <li>Greater value to the business and it's people</li>
      <li>Increased profits and ROI</li>
      <li>Increased brand recognition</li>
      <li>Workplace of choice</li>
    </ul>
  </div>
  <div class="photo photo--team" role="img" aria-label="Photo of a smiling group of diverse office staff standing together"></div>
</section>

</body>
</html>
```